Chewing Gum With Active Ingredients Needs Packaging Design

Brivella Mint Systems is a revolutionary new chewing gum that contains active ingredients commonly found in mouthwashes - it's a portable and convenient way to keep a fresh, clean, and healthy mouth. We have a thorough design brief (attached file) for the packaging we need - a simple sleeve for blister packed gum. We want our design to convey that we are a modern, effective, and high-end product.

Target Market(s)

Young professionals, 20-35 years old

Font styles to use
Serif
Sans Serif

Colors
0292cd
ffffff
0555a3

Requirements
Must have
• A sleek, elegant design
• ALL of the elements listed in the creative brief PDF
• Attached logo
Nice to have
• Incorporation of foil into the design
• A unique, unmistakable look
Should not have
• Too medical of a look

```html
<!DOCTYPE html>
<html lang="en">
<head>
<meta charset="utf-8">
<title>Brivella Mint Systems – Peppermint Gum Sleeve</title>
<link rel="stylesheet" href="https://fonts.googleapis.com/css2?family=Oswald:wght@300;400;500&display=swap">
<style>
  :root {
    --brand-blue: #0292cd;
    --brand-navy: #0555a3;
    --band-blue: #1f9fda;
    --white: #ffffff;
    --stage: #e9e9ea;
    --swirl-silver: #d4d7dc;
    --swirl-ice: #a9c4ef;
    --mint-green: #3f9a3a;
    --mint-light: #7cc36a;
  }
  * { box-sizing: border-box; margin: 0; padding: 0; }
  html, body {
    width: 1200px; height: 1200px; overflow: hidden;
    background: var(--stage);
    font-family: "Oswald", sans-serif;
  }
  .sleeve-front {
    position: absolute; left: 50px; top: 224px;
    width: 1100px; height: 752px;
    background: var(--white);
    overflow: hidden;
  }
  .thumb-cutout {
    position: absolute; right: 0; top: 0;
    width: 1100px; height: 752px;
  }
  .swirl-art {
    position: absolute; left: 0; top: 120px;
    width: 600px; height: 540px;
    background:
      radial-gradient(ellipse 28% 40% at 22% 40%, rgba(169,196,239,.75), transparent 70%),
      radial-gradient(ellipse 22% 30% at 55% 68%, rgba(169,196,239,.6), transparent 70%),
      radial-gradient(ellipse 18% 22% at 78% 85%, rgba(169,196,239,.55), transparent 70%),
      radial-gradient(ellipse 70% 80% at 20% 60%, var(--swirl-silver), transparent 75%);
    border-top-right-radius: 70% 100%;
  }
  .swirl-art.corner {
    left: auto; right: 10px; top: 45px;
    width: 110px; height: 140px;
    border-radius: 50% 50% 40% 60%;
    background:
      radial-gradient(ellipse 45% 50% at 50% 45%, rgba(169,196,239,.7), transparent 75%),
      radial-gradient(ellipse 70% 70% at 50% 50%, var(--swirl-silver), transparent 80%);
  }
  .brand-mark {
    position: absolute; left: 296px; top: 104px;
    display: flex; align-items: center; gap: 20px;
  }
  .brand-mark__dot {
    width: 78px; height: 78px; border-radius: 50%;
    border: 5px solid var(--brand-navy);
  }
  .brand-mark__name {
    font-weight: 300; font-size: 46px; letter-spacing: 4px;
    color: var(--brand-navy); text-transform: uppercase; line-height: 1;
    white-space: nowrap;
  }
  .benefits {
    position: absolute; left: 667px; top: 338px;
    list-style: none;
    color: var(--brand-blue);
    font-weight: 400; font-size: 32px; line-height: 44px;
    letter-spacing: 1px; text-transform: uppercase;
    white-space: nowrap;
  }
  .flavour-band {
    position: absolute; left: 0; bottom: 0;
    width: 100%; height: 102px;
    background: var(--band-blue);
    display: flex; align-items: center;
    color: var(--white);
  }
  .flavour-band__name {
    margin-left: 34px;
    font-weight: 400; font-size: 54px; letter-spacing: 12px;
    white-space: nowrap;
  }
  .flavour-band__claims {
    margin-left: 36px;
    font-weight: 400; font-size: 19px; letter-spacing: 1.5px;
    word-spacing: 3px; white-space: nowrap;
  }
  .mint-leaf-art {
    position: absolute; right: 0; bottom: 0;
    width: 155px; height: 190px;
    border-radius: 60% 30% 0 40%;
    background: radial-gradient(ellipse at 60% 40%, var(--mint-light), var(--mint-green) 75%);
  }
  .pack-count {
    position: absolute; right: 14px; bottom: 18px;
    display: flex; align-items: center; gap: 6px;
    color: var(--white);
  }
  .pack-count__number { font-weight: 500; font-size: 84px; line-height: 1; }
  .pack-count__label {
    font-weight: 400; font-size: 12px; line-height: 24px; letter-spacing: 1px;
  }
</style>
</head>
<body>
  <main class="sleeve-front">
    <div class="swirl-art" role="img" aria-label="Flowing silver and ice-blue wave illustration"></div>
    <div class="swirl-art corner" role="img" aria-label="Small silver and ice-blue wave accent"></div>

    <div class="brand-mark">
      <span class="brand-mark__dot"></span>
      <span class="brand-mark__name">Brivella Mint Systems</span>
    </div>

    <ul class="benefits">
      <li>Whitens teeth</li>
      <li>Freshens breath</li>
      <li>Helps reduce plaque</li>
      <li>Helps protect gums</li>
    </ul>

    <div class="flavour-band">
      <span class="flavour-band__name">PEPPERMINT</span>
      <span class="flavour-band__claims">SUGAR FREE GUM &nbsp;|&nbsp; ASPARTAME FREE &nbsp;|&nbsp; WITH XYLITOL</span>
    </div>

    <div class="mint-leaf-art" role="img" aria-label="Fresh peppermint leaves"></div>
    <div class="pack-count">
      <span class="pack-count__number">8</span>
      <span class="pack-count__label">PIECES<br>SUGAR FREE<br>GUM</span>
    </div>

    <svg class="thumb-cutout" viewBox="0 0 1100 752" aria-hidden="true">
      <ellipse cx="1100" cy="410" rx="62" ry="232" fill="var(--stage)"/>
    </svg>
  </main>
</body>
</html>
```